Lanternway Fellowship (LanFel) University of the Coral Isles, Harbour Rise, Barbados

Seeking an informative and interactive website for the Lanternway Fellowship on campus. The site is mainly to share with prospective students, their families and pastors/ churches what ministry the Society offers its members.

The Lanternway Fellowship (LanFel) is an out reach ministry sponsored by the Leeward Shore Circuit of Lantern Chapels, which is connected to the Lantern Chapel Union of the Tides and Horizons (LCUT) Connexion. The aim of the LanternwayFellowship on the Harbour Rise campus is to mould social justice minded leaders for our region and beyond. Leaders who through their every day lives, seek to serve/ love God and their neighbours through three areas: Faith (spirituality), Mercy (hospitality) & Justice.

I am desiring originally, a six page website, with the option to expand.
Page 1: welcome/ introduction

Page 2: background/ history

Page3: Faith - explains the activities of theLanternwayFellowship that seeks to build and strengthen the faith of its members and that of the campuses generally.

Page 4: Mercy - shares the hospitality offered by the Society to the campus and the students (assistance with settling in to a newish and,school, transportation, edicts assistance, grocery shopping assistance, student foster family programme etc)

Page 5: Justice- shares the social justice activities of the Lanternway Fellowship such as the feeding programme for the homeless in the capital.

Page6: Let's Connect- contact page where students, pastors family members an email us or donate towards our various ministries and where the Societies memorabilia can be displayed and purchased
Updates

Reason: Changes to the brief and including a non refundable payment has led me to extend the deadline til May 6

Target Market(s)

University students usually 18-30 years of age from across the Caribbean region

Industry/Entity Type

University

Number of Pages Required

5+ page

Requirements
Must have
• Ability to play videos and audio

```html
<!DOCTYPE html>
<html lang="en">
<head>
<meta charset="utf-8">
<title>Lanternway Fellowship</title>
<link href="https://fonts.googleapis.com/css2?family=Ubuntu:wght@300;400;500&display=swap" rel="stylesheet">
<style>
:root{
  --page-bg:#edf4cf;
  --card:#ffffff;
  --green:#9dc31f;
  --green-dark:#8ab01a;
  --purple:#5f2a6e;
  --purple-nav:#6f3784;
  --text:#555555;
  --muted:#777777;
  --rule:#dcdcdc;
}
*{margin:0;padding:0;box-sizing:border-box}
html,body{width:705px;height:1200px;overflow:hidden}
body{background:var(--page-bg);font-family:'Ubuntu',sans-serif;color:var(--text);position:relative}
.sheet{position:absolute;left:58px;top:14px;width:589px;height:1166px;background:var(--card);box-shadow:0 1px 4px rgba(0,0,0,.15)}
.abs{position:absolute}
.brand{left:0;width:589px;top:28px;text-align:center;font-size:15px;font-weight:500;color:var(--purple)}
.brand-mark{display:inline-block;width:14px;height:14px;border-radius:50%;background:var(--green);vertical-align:-2px;margin-right:6px}
.nav{left:8px;top:78px;width:574px;height:36px;background:var(--green);display:flex;align-items:center}
.nav a{color:#fff;text-decoration:none;font-size:8.5px;padding:0 13px;height:36px;line-height:36px}
.nav a.active{background:var(--purple-nav);padding:0 19px}
.search{margin-left:auto;margin-right:8px;width:146px;height:18px;border:1px solid #b9d85a;border-radius:9px;background:var(--green-dark);display:flex;align-items:center;justify-content:space-between;padding:0 6px;font-size:6.5px;color:#e6f1c0}
.hero{left:8px;top:114px;width:574px;height:245px;background:linear-gradient(180deg,#5d6470 0%,#8a8c8e 40%,#c9b48a 70%,#2a2723 88%,#111 100%)}
.hero-title{left:343px;top:161px;color:#fff;font-size:18px;font-weight:400}
.dots{left:276px;top:238px;display:flex;gap:4px}
.dots span{width:4px;height:4px;border-radius:50%;background:#fff}
.dots span:first-child{background:var(--purple-nav)}
.welcome-title{left:0;width:589px;top:372px;text-align:center;color:var(--green);font-size:18px;font-weight:400}
.welcome-text{left:8px;width:574px;top:405px;text-align:center;font-size:7.3px;line-height:12px}
.feature{top:474px;width:181px}
.feature .photo{width:181px;height:102px}
.feature h3{font-size:8.3px;font-weight:400;color:var(--green);margin-top:12px}
.feature p{font-size:6.4px;line-height:12px;color:var(--muted);margin-top:7px}
.btn{display:inline-block;background:var(--purple);color:#fff;font-size:6.5px;padding:3px 9px;margin-top:9px}
.section-title{font-size:17px;color:var(--green);font-weight:400}
.arrows{font-size:10px;color:var(--green)}
.rule{height:1px;background:var(--rule)}
.event-photo{left:8px;top:752px;width:147px;height:112px;background:linear-gradient(135deg,#f4efe6,#cdb89e 60%,#8a6f55)}
.ribbon{left:15px;top:752px}
.event-body{left:162px;top:752px;width:176px}
.event-body h4{font-size:8.2px;font-weight:400;color:var(--green);line-height:12px}
.event-body p{font-size:6.3px;line-height:12px;color:var(--muted);margin-top:5px}
.news{left:351px;width:231px}
.news-item{display:flex;gap:9px}
.date{width:41px;height:37px;background:var(--purple);color:#fff;font-size:6px;font-weight:500;text-align:center;line-height:7px;padding-top:9px;flex:none}
.news-item h4{font-size:8.2px;font-weight:400;color:var(--purple);line-height:12px}
.news-item p{font-size:6px;color:var(--muted);margin-top:3px}
.testimonials{left:0;top:908px;width:589px;height:172px;background:var(--green);color:#fff}
.testimonials h2{position:absolute;top:17px;width:100%;text-align:center;font-size:17px;font-weight:400}
.portrait{left:37px;top:50px;width:104px;height:104px;border-radius:50%;background:linear-gradient(180deg,#cfd2d4,#5a6677)}
.quote-mark{left:159px;top:60px;font-size:12px;font-weight:500}
.name{left:159px;top:75px;font-size:11px;font-weight:500}
.quote{left:159px;top:94px;width:402px;font-size:6.6px;line-height:12px;color:#f3f8e0}
.tarrow{top:82px;font-size:11px}
.social{left:271px;top:1097px;display:flex;gap:2px}
.social span{width:21px;height:21px;border-radius:50%;border:1.5px solid #3b6ea8}
.footer-links{left:0;width:589px;top:1122px;text-align:center;font-size:8px;color:#666;word-spacing:1px}
.copyright{left:0;width:589px;top:1141px;text-align:center;font-size:7.8px;color:#666}
</style>
</head>
<body>
<div class="sheet">
  <div class="abs brand"><span class="brand-mark"></span>Lanternway Fellowship</div>

  <nav class="abs nav">
    <a class="active">Home</a><a>Welcome</a><a>Background</a><a>Faith</a><a>Mercy</a><a>Justice</a><a>Lets Connect</a>
    <div class="search"><span>Search</span>
      <svg width="7" height="7" viewBox="0 0 10 10"><circle cx="4" cy="4" r="3" fill="none" stroke="#fff" stroke-width="1.5"/><line x1="6.3" y1="6.3" x2="9" y2="9" stroke="#fff" stroke-width="1.5"/></svg>
    </div>
  </nav>

  <div class="abs hero" role="img" aria-label="Silhouette of a person with raised arms on a grassy hill at sunset">
    <div class="abs hero-title">Lanternway Fellowship</div>
    <div class="abs dots"><span></span><span></span><span></span><span></span></div>
  </div>

  <h1 class="abs welcome-title">Welcome to Lanternway Fellowship</h1>
  <p class="abs welcome-text">The Lanternway Fellowship (LanFel) is an out reach ministry sponsored by the Leeward Shore Circuit of Lantern Chapels, which is connected to the Lantern Chapel Union of the Tides and Horizons (LCUT) Connexion. The aim of the LanternwayFellowship on the Harbour Rise campus is to mould social justice minded leaders for our region and beyond.Leaders who through their every day lives, seek to serve/ love God and their neighbours</p>

  <div class="abs feature" style="left:8px">
    <div class="photo" role="img" aria-label="Silhouette of one person helping another up against an orange sunset" style="background:linear-gradient(180deg,#e88a1c,#c2410c 60%,#2a1205)"></div>
    <h3>Faith (spirituality)</h3>
    <p>Lorem Ipsum is simply dummy text of the printing and typesetting industry. Lorem Ipsum has been the industry's standard dummy text ever</p>
    <span class="btn">Read More</span>
  </div>
  <div class="abs feature" style="left:204px">
    <div class="photo" role="img" aria-label="Black and white photo of hands pressed together in prayer" style="background:linear-gradient(135deg,#2b2b2b,#9a9a9a 55%,#d8d8d8)"></div>
    <h3>Mercy (hospitality)</h3>
    <p>Lorem Ipsum is simply dummy text of the printing and typesetting industry. Lorem Ipsum has been the industry's standard dummy text ever</p>
    <span class="btn">Read More</span>
  </div>
  <div class="abs feature" style="left:400px">
    <div class="photo" role="img" aria-label="Bronze scales of justice" style="background:linear-gradient(135deg,#f4f1ec,#c9a987 55%,#6b4a2c)"></div>
    <h3>Justice</h3>
    <p>Lorem Ipsum is simply dummy text of the printing and typesetting industry. Lorem Ipsum has been the industry's standard dummy text ever</p>
    <span class="btn">Read More</span>
  </div>

  <h2 class="abs section-title" style="left:8px;top:710px">Events</h2>
  <div class="abs arrows" style="left:324px;top:714px">&lsaquo; &rsaquo;</div>
  <div class="abs rule" style="left:8px;top:738px;width:330px"></div>
  <div class="abs event-photo" role="img" aria-label="Hand reaching up toward bright light"></div>
  <svg class="abs ribbon" width="34" height="40" viewBox="0 0 34 40">
    <path d="M0 0H34V40L17 32L0 40Z" fill="#9dc31f"/>
    <text x="17" y="16" text-anchor="middle" font-family="Ubuntu,sans-serif" font-size="6.5" font-weight="500" fill="#fff">APRIL</text>
    <text x="17" y="23" text-anchor="middle" font-family="Ubuntu,sans-serif" font-size="6.5" font-weight="500" fill="#fff">2015</text>
  </svg>
  <div class="abs event-body">
    <h4>Lorem Ipsum is simply dummy text of the printing and typesetting industry.</h4>
    <p>Lorem Ipsum is simply dummy text of the printing and typesetting industry. Lorem Ipsum has been the industry's standard dummy text ever since the 1500s, when an unknown printer took a galley of type and scrambled it to make a type specimen book.</p>
    <span class="btn" style="margin-top:6px">Read More</span>
  </div>

  <h2 class="abs section-title" style="left:350px;top:710px">Latest News</h2>
  <div class="abs arrows" style="left:570px;top:714px">&lsaquo; &rsaquo;</div>
  <div class="abs rule" style="left:351px;top:738px;width:231px"></div>
  <div class="abs news" style="top:752px">
    <div class="news-item"><div class="date">25TH<br>APRIL<br>2015</div><div><h4>Lorem Ipsum is simply dummy text of the printing and typesetting industry.</h4><p>Lorem Ipsum has been the industry's standard</p></div></div>
  </div>
  <div class="abs rule" style="left:351px;top:804px;width:231px"></div>
  <div class="abs news" style="top:821px">
    <div class="news-item"><div class="date">25TH<br>APRIL<br>2015</div><div><h4>Lorem Ipsum is simply dummy text of the printing and typesetting industry.</h4><p>Lorem Ipsum has been the industry's standard</p></div></div>
  </div>

  <section class="abs testimonials">
    <h2>Testimonials</h2>
    <div class="abs tarrow" style="left:9px">&lsaquo;</div>
    <div class="abs tarrow" style="left:574px">&rsaquo;</div>
    <div class="abs portrait" role="img" aria-label="Portrait of a smiling man in a suit and tie"></div>
    <div class="abs quote-mark">&ldquo;</div>
    <div class="abs name">Marcus Ellery</div>
    <p class="abs quote">Lorem Ipsum is simply dummy text of the printing and typesetting industry. Lorem Ipsum has been the industry's standard dummy text ever since the 1500s, when an unknown printer took a galley of type and scrambled it to make a type specimen book. It has survived not only five centuries, but also the leap into electronic typesetting, remaining essentially unchanged.</p>
  </section>

  <div class="abs social"><span></span><span></span></div>
  <div class="abs footer-links">Home &nbsp;&nbsp;|&nbsp;&nbsp; Welcome &nbsp;&nbsp;|&nbsp;&nbsp; Background &nbsp;&nbsp;|&nbsp;&nbsp; Faith &nbsp;&nbsp;|&nbsp;&nbsp; Mercy &nbsp;&nbsp;|&nbsp;&nbsp; Justice &nbsp;&nbsp;|&nbsp;&nbsp; Lets Connect</div>
  <div class="abs copyright">&copy; 2015 Company Name .All Rights Reserved</div>
</div>
</body>
</html>
```